Harlow Creek Church Invite Card

We are a vibrant multigenerational church outside of Raleigh, NC and are wanting a 'church invite card' that we can encourage our members to carry with them so that they can invite their friends to church.

These cards should have a modern feel (see http://zentravio.com/neat-card-ideas/ for the feel we are going for), match the branding of our website (www.harlowcreek.org) and include the following information on the back:

Service Times: Sunday @ 8:30 AM and 11:00 AM (Main Focus)
Website: www.harlowcreek.org (Main Focus)
Social Media: (You can simply use the icons for these if desired)
www.plazebook.example/harlowcreekchurch
www.snapgrove.example/harlowcreekchurch
www.vidstream.example/harlowcreekyouth
Address: 4827 Marlow Avenue Fairbrook, NC 27500 (Not a main focus)
Phone: (555) 555-0182 (Not a main focus)

The front should simply say 'We look forward to meeting you!'

Logos: Attached you will find the necessary logos for this project.

Fonts and Colors: Here are the specific colors (See HCC_Website_Color_Palette.pdf) and fonts that are used on our website.
Pacifico
Helvetica
Open Sans Regular

Target Market(s)

Friends of our congregation

Industry/Entity Type

Church

Contact Information for Business Card

We will likely print through Quillby Printworks. The details of what they need can be found here: http://www.quillbyprint.example/products/business-card

Font styles to use
Other font styles liked:
• Pacifico, Helvetica, Open Sans Regular, Bebas Nue

Colors
0592cd
34a7d8
85cae6
cee9f5
0455a3
3176b5
85acd3
cfdfed

Requirements
Must have
• Sleek, eye catching design
Nice to have
• Rounded Corners, Our social media sites (PB, Snapg and VidStream)

```html
<!DOCTYPE html>
<html lang="en">
<head>
<meta charset="utf-8">
<title>Harlow Creek Church – Invite Card</title>
<link rel="stylesheet" href="https://fonts.googleapis.com/css2?family=Arimo:wght@400;700&display=swap">
<style>
  :root {
    --page-bg: #ecebe8;
    --card-white: #f7f7f7;
    --brand-blue: #1583c9;
    --accent-blue: #3a63b0;
    --ink: #1b1b1b;
    --ink-soft: #2c2c2c;
    --on-blue: #ffffff;
    --social-dark: #3b5a99;
    --social-mid: #8a7560;
    --social-red: #c4302b;
  }
  * { box-sizing: border-box; margin: 0; padding: 0; }
  html, body { width: 1200px; height: 864px; overflow: hidden; }
  body {
    background: var(--page-bg);
    font-family: "Arimo", Helvetica, Arial, sans-serif;
    color: var(--ink);
    position: relative;
  }
  .card {
    position: absolute;
    top: 278px;
    width: 540px;
    height: 309px;
    border-radius: 10px;
    box-shadow: 0 6px 18px rgba(0,0,0,0.18);
    overflow: hidden;
  }

  /* Front: contact side */
  .card-front { left: 40px; background: var(--card-white); }
  .card-front .brand {
    position: absolute; left: 34px; top: 34px;
    display: flex; align-items: center; gap: 10px;
  }
  .card-front .brand-mark {
    width: 14px; height: 14px; border-radius: 50%;
    background: var(--accent-blue); flex: none;
  }
  .card-front .brand-name {
    font-size: 28px; font-weight: 700; color: var(--ink);
    letter-spacing: 0.5px; white-space: nowrap;
  }
  .card-front .divider {
    position: absolute; left: 0; top: 96px;
    width: 330px; height: 2px; background: var(--ink);
  }
  .person {
    position: absolute; right: 40px; top: 112px; text-align: right;
  }
  .person-name { font-size: 19px; font-weight: 700; color: var(--accent-blue); }
  .person-role { font-size: 13px; color: var(--ink); margin-top: 4px; }
  .contact-list {
    position: absolute; left: 30px; top: 176px;
    list-style: none; font-size: 12.5px; color: var(--ink-soft); line-height: 19px;
  }
  .contact-list li { display: flex; align-items: center; gap: 7px; white-space: nowrap; }
  .contact-list svg { width: 11px; height: 11px; flex: none; }
  .contact-list .invite-line { font-size: 13px; color: var(--ink); margin-top: 2px; }
  .social-list {
    position: absolute; right: 40px; bottom: 30px;
    display: flex; gap: 14px; list-style: none;
    font-size: 12px; font-weight: 700;
  }
  .social-list li { display: flex; align-items: center; gap: 5px; color: var(--ink-soft); }
  .social-list .dot { width: 10px; height: 10px; border-radius: 2px; }
  .dot-pb { background: var(--social-dark); }
  .dot-snapg { background: var(--social-mid); }
  .dot-vid { background: var(--social-red); }

  /* Back: service side */
  .card-back { left: 620px; background: var(--brand-blue); color: var(--on-blue); }
  .card-back .brand {
    position: absolute; left: 0; right: 0; top: 100px;
    display: flex; justify-content: center; align-items: center; gap: 12px;
  }
  .card-back .brand-mark {
    width: 16px; height: 16px; border-radius: 50%;
    background: var(--on-blue); flex: none;
  }
  .card-back .brand-name {
    font-size: 32px; font-weight: 700; color: var(--on-blue);
    letter-spacing: 0.5px; white-space: nowrap;
  }
  .card-back .service-times {
    position: absolute; left: 0; right: 0; top: 180px;
    text-align: center; font-size: 17px; color: var(--on-blue); white-space: nowrap;
  }
</style>
</head>
<body>
  <section class="card card-front" aria-label="Invite card front">
    <div class="brand">
      <span class="brand-mark" aria-hidden="true"></span>
      <span class="brand-name">Harlow Creek Church</span>
    </div>
    <div class="divider"></div>
    <div class="person">
      <div class="person-name">Martin Ellery</div>
      <div class="person-role">Managing Director</div>
    </div>
    <ul class="contact-list">
      <li>
        <svg viewBox="0 0 12 12" aria-hidden="true"><rect width="12" height="12" rx="2" fill="#3a63b0"/><path d="M3.5 3h1.6l.6 1.6-.9.7a4.5 4.5 0 0 0 2 2l.7-.9 1.6.6V8.6c0 .4-.4.8-.8.7A6 6 0 0 1 2.8 3.8c0-.4.3-.8.7-.8z" fill="#fff"/></svg>
        (555) 555-0182
      </li>
      <li>
        <svg viewBox="0 0 12 12" aria-hidden="true"><rect width="12" height="12" rx="2" fill="#3a63b0"/><circle cx="6" cy="6" r="3.3" fill="none" stroke="#fff" stroke-width="1"/><path d="M2.7 6h6.6M6 2.7c-1.6 2-1.6 4.6 0 6.6M6 2.7c1.6 2 1.6 4.6 0 6.6" fill="none" stroke="#fff" stroke-width=".8"/></svg>
        www.harlowcreek.org
      </li>
      <li>
        <svg viewBox="0 0 12 12" aria-hidden="true"><rect width="12" height="12" rx="2" fill="#3a63b0"/><path d="M6 2.3a2.6 2.6 0 0 1 2.6 2.6C8.6 6.8 6 9.7 6 9.7S3.4 6.8 3.4 4.9A2.6 2.6 0 0 1 6 2.3z" fill="#fff"/><circle cx="6" cy="4.9" r="1" fill="#3a63b0"/></svg>
        4827 Marlow Avenue Fairbrook, NC 27500
      </li>
      <li class="invite-line">'We look forward to meeting you!'</li>
    </ul>
    <ul class="social-list">
      <li><span class="dot dot-pb"></span>PB</li>
      <li><span class="dot dot-snapg"></span>Snapg</li>
      <li><span class="dot dot-vid"></span>VidStream</li>
    </ul>
  </section>

  <section class="card card-back" aria-label="Invite card back">
    <div class="brand">
      <span class="brand-mark" aria-hidden="true"></span>
      <span class="brand-name">Harlow Creek Church</span>
    </div>
    <p class="service-times">Service Times: Sunday @ 8:30 AM and 11:00 AM</p>
  </section>
</body>
</html>
```